Veterinary Business cards

Redesign Business Card

Information needed on Card:
Hours: Mon-Fri: 4pm -10PM; Sat- Sun- 10 AM- 5PM
Help@tandrelyns.com
www.tandrelyns.com
405-718-2954
4170 SW 38th Ave. okc, ok 73119
*No appointment necessary*

Optional:
Our tag line is "We're here when you need us" - If it fits on the cards.

```html
<!DOCTYPE html>
<html lang="en">
<head>
<meta charset="utf-8">
<title>Tandrelyn Pet Urgent Care – Business Card</title>
<link href="https://fonts.googleapis.com/css2?family=Arimo:wght@400;700&display=swap" rel="stylesheet">
<style>
  :root {
    --navy: #0d2d5c;
    --navy-deep: #08234d;
    --orange: #e07b1a;
    --white: #ffffff;
    --backdrop: #e6e7e9;
  }
  * { margin: 0; padding: 0; box-sizing: border-box; }
  html, body { width: 1200px; height: 800px; overflow: hidden; }
  body {
    background: var(--backdrop);
    font-family: "Arimo", Arial, sans-serif;
    display: flex;
    flex-direction: column;
    align-items: center;
    justify-content: center;
    gap: 40px;
  }
  .card {
    width: 630px;
    height: 340px;
    border-radius: 26px;
    background: linear-gradient(135deg, var(--navy) 0%, var(--navy-deep) 100%);
    box-shadow: 0 3px 0 var(--orange);
    position: relative;
    color: var(--white);
  }
  .brand { display: flex; align-items: center; gap: 12px; }
  .brand-dot {
    width: 18px; height: 18px; border-radius: 50%;
    background: var(--orange); flex: none;
  }
  .brand-name {
    font-weight: 400;
    color: var(--white);
    letter-spacing: 1px;
    line-height: 1.15;
  }

  /* Contact side */
  .card-contact .brand { position: absolute; left: 60px; top: 140px; }
  .card-contact .brand-name { font-size: 26px; width: 230px; }
  .contact {
    position: absolute; left: 355px; top: 38px; right: 30px;
  }
  .person-name { font-size: 24px; font-weight: 700; letter-spacing: .5px; }
  .person-role { font-size: 16px; color: var(--orange); margin: 2px 0 14px; }
  .contact-list { list-style: none; font-size: 15px; line-height: 1.35; }
  .contact-list li { display: flex; gap: 10px; margin-bottom: 4px; }
  .contact-list svg { width: 14px; height: 14px; flex: none; margin-top: 2px; fill: var(--orange); }
  .walk-in {
    margin-top: 8px;
    font-size: 14px;
    font-weight: 700;
    color: var(--orange);
  }

  /* Logo side */
  .card-logo { display: flex; flex-direction: column; align-items: center; justify-content: center; }
  .card-logo .brand-name { font-size: 40px; }
  .card-logo .brand { margin-top: -20px; }
  .tagline {
    position: absolute; bottom: 48px; left: 0; right: 0;
    text-align: center; font-size: 17px;
  }
  .tagline em { font-style: normal; color: var(--orange); }
</style>
</head>
<body>
  <section class="card card-contact">
    <div class="brand">
      <span class="brand-dot"></span>
      <span class="brand-name">Tandrelyn Pet Urgent Care</span>
    </div>
    <div class="contact">
      <p class="person-name">DANIEL HARPER</p>
      <p class="person-role">President</p>
      <ul class="contact-list">
        <li>
          <svg viewBox="0 0 24 24"><path d="M12 2a7 7 0 0 0-7 7c0 5 7 13 7 13s7-8 7-13a7 7 0 0 0-7-7zm0 9.5A2.5 2.5 0 1 1 12 6.5a2.5 2.5 0 0 1 0 5z"/></svg>
          <span>4170 SW 38th Ave.<br>okc, ok 73119</span>
        </li>
        <li>
          <svg viewBox="0 0 24 24"><path d="M6.6 10.8a15 15 0 0 0 6.6 6.6l2.2-2.2a1 1 0 0 1 1-.25 11.4 11.4 0 0 0 3.6.57 1 1 0 0 1 1 1V20a1 1 0 0 1-1 1A17 17 0 0 1 3 4a1 1 0 0 1 1-1h3.5a1 1 0 0 1 1 1c0 1.25.2 2.450.57 3.6a1 1 0 0 1-.25 1z"/></svg>
          <span>405-718-2954</span>
        </li>
        <li>
          <svg viewBox="0 0 24 24"><path d="M2 5h20v14H2zm2 2v.5l8 5 8-5V7l-8 5z"/></svg>
          <span>Help@tandrelyns.com</span>
        </li>
        <li>
          <svg viewBox="0 0 24 24"><path d="M12 2a10 10 0 1 0 0 20 10 10 0 0 0 0-20zm0 2a8 8 0 0 1 7.7 6H4.3A8 8 0 0 1 12 4zm-7.7 8h15.4a8 8 0 0 1-15.4 2z"/></svg>
          <span>www.tandrelyns.com</span>
        </li>
        <li>
          <svg viewBox="0 0 24 24"><path d="M12 2a10 10 0 1 0 0 20 10 10 0 0 0 0-20zm0 2a8 8 0 1 1 0 16 8 8 0 0 1 0-16zm-1 3v6l5 3 1-1.6-4-2.4V7z"/></svg>
          <span>Mon–Fri: 4 PM – 10 PM<br>Sat–Sun: 10 AM – 5 PM</span>
        </li>
      </ul>
      <p class="walk-in">*No appointment necessary*</p>
    </div>
  </section>

  <section class="card card-logo">
    <div class="brand">
      <span class="brand-dot"></span>
      <span class="brand-name">Tandrelyn Pet Urgent Care</span>
    </div>
    <p class="tagline">We're here <em>when you need us</em></p>
  </section>
</body>
</html>
```